Willowbend Pharmacy Business Cards

I need a business card design and or template. Needs to convey a softer feel along with health and wellness. Please see attached logo and color scheme.

Industry/Entity Type

Pharmacy

Colors

Designer to choose colors to be used in the design.

Requirements
Must have
• I've added a second NEW colored logo I think I am going to go with the blue green logo.
• Needs to have the colors and feel of the logo attached.
• Darrel Quimby
• Pharmacy Manager
• willowbendpharmacy.example

```html
<!DOCTYPE html>
<html lang="en">
<head>
<meta charset="utf-8">
<title>Willowbend Pharmacy Business Cards</title>
<link rel="stylesheet" href="https://fonts.googleapis.com/css2?family=Arimo:ital,wght@0,400;1,700&family=Outfit:wght@600&display=swap">
<style>
  :root {
    --backdrop: #34434c;
    --green-deep: #1f7a3a;
    --green-bright: #5cb23f;
    --lime: #a9cf45;
    --pink: #e9708f;
    --slate: #6d7377;
    --ink: #111111;
    --charcoal: #2a2420;
    --stone: #8a8c8e;
  }
  * { box-sizing: border-box; margin: 0; padding: 0; }
  html, body { width: 1200px; height: 800px; overflow: hidden; }
  body {
    background: var(--backdrop);
    display: flex;
    flex-direction: column;
    align-items: center;
    justify-content: center;
    gap: 30px;
  }
  .card {
    position: relative;
    width: 630px;
    height: 360px;
    overflow: hidden;
    box-shadow: 0 10px 24px rgba(0,0,0,0.35);
  }
  .card-front {
    background: linear-gradient(200deg, var(--green-bright) 0%, #3f9a3c 45%, var(--green-deep) 100%);
  }
  .front-accent {
    position: absolute;
    top: 0;
    left: 255px;
    width: 80px;
    height: 100%;
    background: linear-gradient(90deg, rgba(109,115,119,0.35), rgba(233,112,143,0.35));
  }
  .holder-name {
    position: absolute;
    top: 14px;
    right: 26px;
    text-align: center;
    color: var(--ink);
  }
  .holder-name__name {
    font-family: "Arimo", Arial, sans-serif;
    font-weight: 700;
    font-style: italic;
    font-size: 30px;
    letter-spacing: 1.5px;
    text-transform: uppercase;
    line-height: 1;
  }
  .holder-name__role {
    font-family: "Arimo", Arial, sans-serif;
    font-size: 17px;
    margin-top: 2px;
  }
  .front-brand {
    position: absolute;
    left: 28px;
    top: 132px;
    display: flex;
    align-items: center;
    gap: 10px;
    font-family: "Outfit", sans-serif;
    font-weight: 600;
    font-size: 19px;
    line-height: 1.15;
    color: var(--pink);
  }
  .brand-dot {
    width: 34px;
    height: 34px;
    border-radius: 50%;
    background: var(--lime);
    flex: none;
  }
  .front-url {
    position: absolute;
    right: 22px;
    bottom: 16px;
    font-family: "Arimo", Arial, sans-serif;
    font-size: 22px;
    color: var(--lime);
  }
  .card-back { background: var(--charcoal); }
  .back-brand {
    position: absolute;
    inset: 0;
    display: flex;
    align-items: center;
    justify-content: center;
    gap: 22px;
  }
  .back-brand .brand-dot { width: 90px; height: 90px; background: var(--pink); }
  .back-brand__name {
    font-family: "Outfit", sans-serif;
    font-weight: 600;
    font-size: 44px;
    line-height: 1.05;
    color: var(--stone);
  }
</style>
</head>
<body>
  <section class="card card-front" aria-label="Business card front">
    <div class="front-accent" role="img" aria-label="Decorative accent band in grey and pink"></div>
    <div class="holder-name">
      <p class="holder-name__name">Darrel Quimby</p>
      <p class="holder-name__role">Pharmacy Manager</p>
    </div>
    <div class="front-brand">
      <span class="brand-dot"></span>
      <span>Willowbend<br>Pharmacy</span>
    </div>
    <p class="front-url">willowbendpharmacy.example</p>
  </section>

  <section class="card card-back" aria-label="Business card back">
    <div class="back-brand">
      <span class="brand-dot"></span>
      <p class="back-brand__name">Willowbend<br>Pharmacy</p>
    </div>
  </section>
</body>
</html>
```